Ledgerwise Business Card Design

Business Card Design for new business called Ledgerwise focused on selling business software to small and medium size companies who have outgrown Tallymark. Similar companies would be Tallymark, Nuvo, CoreFlow. Also Dealharbor would be good to look at for additional ideas around look and feel.

Target Market(s)

Business to Business

Industry/Entity Type

Information Technology

Contact Information for Business Card

Standard Business Card Information

Font styles to use
Sans Serif

```html
<!DOCTYPE html>
<html lang="en">
<head>
<meta charset="utf-8">
<title>Ledgerwise Stationery</title>
<link href="https://fonts.googleapis.com/css2?family=Montserrat:wght@600&family=Open+Sans:wght@400;600&display=swap" rel="stylesheet">
<style>
  :root {
    --navy: #20577d;
    --orange: #e2852f;
    --paper: #f7f7f7;
    --backdrop: #e6e6e6;
    --ink: #3c4650;
    --muted: #6d7680;
    --rule: #b5bcc3;
  }
  * { box-sizing: border-box; margin: 0; padding: 0; }
  html, body { width: 1200px; height: 795px; overflow: hidden; }
  body {
    background: var(--backdrop);
    font-family: "Open Sans", Arial, sans-serif;
    color: var(--ink);
    position: relative;
  }
  .piece { position: absolute; }
  .wordmark {
    font-family: "Montserrat", Arial, sans-serif;
    font-weight: 600;
    display: flex;
    align-items: center;
    gap: 0.35em;
    white-space: nowrap;
    letter-spacing: -0.01em;
  }
  .wordmark .dot {
    width: 0.7em; height: 0.7em;
    border-radius: 50%;
    background: var(--orange);
    flex: none;
  }
  .on-paper { color: var(--navy); }
  .on-navy { color: #f2f2f2; }

  .contact { font-size: 5.4px; line-height: 1.45; color: var(--ink); }
  .contact-row { display: flex; align-items: center; gap: 3px; }
  .contact-row svg { width: 5px; height: 5px; fill: var(--navy); flex: none; }

  /* letterhead */
  .letterhead { left: 292px; top: 99px; width: 294px; height: 414px; background: var(--paper); }
  .letterhead .wordmark { position: absolute; left: 18px; top: 32px; font-size: 12px; }
  .letterhead .contact {
    position: absolute; left: 208px; top: 22px;
    padding-left: 6px; border-left: 0.6px solid var(--rule);
  }
  .letterhead .site {
    position: absolute; bottom: 10px; width: 100%; text-align: center;
    font-size: 5.2px; letter-spacing: 0.22em; color: var(--muted);
  }

  /* folder */
  .folder { left: 635px; top: 80px; width: 347px; height: 437px; background: var(--navy); }
  .folder .spine { position: absolute; left: 0; top: 0; width: 19px; height: 100%; background: var(--orange); }
  .folder .wordmark { position: absolute; left: 77px; top: 198px; font-size: 30px; }

  /* business cards */
  .card { width: 133px; height: 75px; }
  .card-front { left: 186px; top: 550px; background: var(--paper); overflow: hidden; }
  .card-front .wordmark { position: absolute; left: 8px; top: 32px; font-size: 7.8px; }
  .card-front .details {
    position: absolute; left: 70px; top: 19px;
    padding-left: 4px; border-left: 0.6px solid var(--rule);
  }
  .card-front .name { font-size: 5.4px; font-weight: 600; color: var(--navy); letter-spacing: 0.02em; line-height: 1.3; }
  .card-front .role { font-size: 4.2px; color: var(--orange); margin-bottom: 2px; line-height: 1.3; }
  .card-front .contact { font-size: 4px; line-height: 1.4; }
  .card-front .contact-row svg { width: 4px; height: 4px; }
  .card-back { left: 186px; top: 647px; background: var(--navy); }
  .card-back .wordmark { position: absolute; left: 0; right: 0; top: 31px; justify-content: center; font-size: 10px; }

  /* envelopes */
  .envelope { width: 328px; height: 157px; background: var(--paper); }
  .envelope-front { left: 354px; top: 562px; }
  .envelope-front .wordmark { position: absolute; left: 14px; top: 23px; font-size: 11px; }
  .envelope-front .contact { position: absolute; left: 14px; top: 44px; font-size: 5.6px; }
  .envelope-back { left: 714px; top: 562px; }
  .envelope-back .flap { position: absolute; left: 0; top: 0; width: 328px; height: 56px; }
  .envelope-back .wordmark { position: absolute; left: 0; right: 0; top: 22px; justify-content: center; font-size: 11px; }
</style>
</head>
<body>

  <section class="piece letterhead" aria-label="Letterhead">
    <div class="wordmark on-paper"><span>Ledgerwise</span><span class="dot"></span></div>
    <div class="contact">
      <div>412 Alder Court</div>
      <div>Juneau, Alaska 34580</div>
      <div class="contact-row" style="margin-top:3px"><svg viewBox="0 0 10 10"><path d="M2 0h2l1 3-1.5 1a6 6 0 0 0 2.5 2.5L7 5l3 1v2c0 1-1 2-2 2A8 8 0 0 1 0 2c0-1 1-2 2-2z"/></svg>555 210 4836</div>
      <div class="contact-row"><svg viewBox="0 0 10 10"><rect x="2" y="1" width="6" height="3"/><rect x="0" y="4" width="10" height="5"/></svg>555 318 7702</div>
      <div class="contact-row"><svg viewBox="0 0 10 10"><path d="M0 2h10v6H0z"/></svg>mail@ledgerwise.co</div>
    </div>
    <div class="site">www.ledgerwise.co</div>
  </section>

  <section class="piece folder" aria-label="Presentation folder">
    <div class="spine"></div>
    <div class="wordmark on-navy"><span>Ledgerwise</span><span class="dot"></span></div>
  </section>

  <section class="piece card card-front" aria-label="Business card front">
    <div class="wordmark on-paper"><span>Ledgerwise</span><span class="dot"></span></div>
    <div class="details">
      <div class="name">MARA ELLISON</div>
      <div class="role">CEO/Founder</div>
      <div class="contact">
        <div>412 Alder Court</div>
        <div>Juneau, Alaska 34580</div>
        <div class="contact-row"><svg viewBox="0 0 10 10"><path d="M2 0h2l1 3-1.5 1a6 6 0 0 0 2.5 2.5L7 5l3 1v2c0 1-1 2-2 2A8 8 0 0 1 0 2c0-1 1-2 2-2z"/></svg>555 210 4836</div>
        <div class="contact-row"><svg viewBox="0 0 10 10"><rect x="2" y="1" width="6" height="3"/><rect x="0" y="4" width="10" height="5"/></svg>555 318 7702</div>
        <div class="contact-row"><svg viewBox="0 0 10 10"><path d="M0 2h10v6H0z"/></svg>mail@ledgerwise.co</div>
        <div class="contact-row"><svg viewBox="0 0 10 10"><circle cx="5" cy="5" r="5"/></svg>www.ledgerwise.co</div>
      </div>
    </div>
  </section>

  <section class="piece card card-back" aria-label="Business card back">
    <div class="wordmark on-navy"><span>Ledgerwise</span><span class="dot"></span></div>
  </section>

  <section class="piece envelope envelope-front" aria-label="Envelope front">
    <div class="wordmark on-paper"><span>Ledgerwise</span><span class="dot"></span></div>
    <div class="contact">
      <div>412 Alder Court</div>
      <div>Juneau, Alaska 34580</div>
    </div>
  </section>

  <section class="piece envelope envelope-back" aria-label="Envelope back">
    <svg class="flap" viewBox="0 0 328 56" preserveAspectRatio="none">
      <path d="M0 0H328L323 48Q322 55 314 55H14Q6 55 5 48Z" fill="var(--navy)"/>
    </svg>
    <div class="wordmark on-navy"><span>Ledgerwise</span><span class="dot"></span></div>
  </section>

</body>
</html>
```